Weight loss surgery restaurant card

We need to create a card for patients who have undergone weight loss surgery to take to restaurants so they can request smaller meals. These patients have had surgery on their stomach so that they can only consume half to one cup of food at a time. So normal sized restaurant meals are way too big (and cost a lot). This card they can present to the restaurant to communicate the fact that they have had weight loss surgery and therefore request a smaller meal portion at reduced cost

Target Market(s)

Restaurants serving weight loss surgery patients

Industry/Entity Type

Health Care

Contact Information for Business Card

This will be a plastic card similar to business card size.

Requirements
Must have
• The front of the card should include the following text:
• The individual bearing this card has undergone weight loss surgery.
• This surgery restricts portion sizes to between half and one cup of food at a time.
• Please give consideration to allowing smaller portions of your regular meals to be ordered to reduce wastage and excess costs.
• Example: a half size portion priced at two thirds of usual cost.
• The back of the card will have spaces for the person to write certain information. These are the categories that can be filled in by hand:
• Name:
• Procedure performed:
• Date of procedure (month/year):
• Treating Clinic Name:
• Treating Clinic Signature:
• Somewhere down the bottom should be something along the lines of:
• supplied from bernardwhitlow.com.au
Nice to have
• A nice design with imagery/colours etc ... not just the text on a white background! Bright attractive colours preferred.
• I have uploaded my logo ... a roughly triangular image followed by my name etc. The triangular logo image could be used somewhere on the card and this logo can be interchangeable for other clinics who purchase the card.
• **Please note that I don't want my name to be included as part of the logo on the card ... just use the triangular image on the side of the logo without the following name**
• Also, the colouring of the card does not have to reflect my logo colours as I am anticipating interchanging this logo with other logos if other clinics choose to adopt the card. I am interested to see other, more generic, colour choices as well as my logo colours

```html
<!DOCTYPE html>
<html lang="en">
<head>
<meta charset="utf-8">
<title>Weight Loss Surgery Restaurant Card</title>
<link href="https://fonts.googleapis.com/css2?family=Ubuntu:wght@400;500&display=swap" rel="stylesheet">
<style>
  :root {
    --bg: #e5e5e5;
    --teal: #17918a;
    --teal-light: #67aca7;
    --yellow: #fdbf00;
    --red: #d56060;
    --dark: #333333;
    --darker: #262626;
    --white: #ffffff;
  }
  * { margin: 0; padding: 0; box-sizing: border-box; }
  html, body {
    width: 1200px; height: 1200px; overflow: hidden;
    background: var(--bg);
    font-family: "Ubuntu", sans-serif;
  }
  .card {
    position: absolute; left: 170px;
    width: 860px; height: 504px;
    background: var(--white);
    box-shadow: 18px 22px 30px rgba(0,0,0,0.18);
    overflow: hidden;
  }
  .card-front { top: 66px; }
  .card-back { top: 630px; }
  .card-art { position: absolute; inset: 0; width: 100%; height: 100%; }

  .ribbon {
    position: absolute; color: var(--white);
    display: flex; align-items: center;
    font-size: 14px; line-height: 1.3;
  }
  .ribbon-intro {
    left: 184px; top: 76px; width: 631px; height: 39px;
    background: var(--dark); justify-content: flex-end;
    padding-right: 13px; font-size: 15px; font-weight: 500;
    clip-path: polygon(0 0, 100% 0, 100% 100%, 39px 100%);
  }
  .ribbon-restriction {
    left: 240px; top: 131px; width: 575px; height: 41px;
    background: var(--yellow); padding-left: 87px;
    clip-path: polygon(0 0, 100% 0, 100% 100%, 41px 100%);
  }
  .ribbon-request {
    left: 292px; top: 188px; width: 522px; height: 54px;
    background: var(--teal-light); padding-left: 32px;
    clip-path: polygon(0 0, 100% 0, 100% 100%, 12px 100%, 12px 15px);
  }
  .ribbon-example {
    left: 305px; top: 259px; width: 510px; height: 41px;
    background: var(--red); padding-left: 32px;
  }

  .clinic-name {
    position: absolute; left: 62px; top: 363px;
    display: flex; align-items: center; gap: 10px;
    color: var(--white); font-size: 22px; font-weight: 500;
  }
  .clinic-dot {
    width: 18px; height: 18px; border-radius: 50%;
    background: var(--teal);
  }

  .field {
    position: absolute; left: 58px; right: 59px; height: 40px;
    display: flex; align-items: center;
  }
  .field-label {
    color: var(--dark); font-size: 23px; white-space: nowrap;
  }
  .field-line { position: absolute; right: 0; top: 0; height: 40px; }
  .field-name { top: 78px; }
  .field-name .field-line { left: 271px; background: var(--teal); }
  .field-procedure { top: 142px; }
  .field-procedure .field-line { left: 271px; background: var(--dark); }
  .field-date { top: 203px; }
  .field-date .field-line { left: 374px; background: var(--yellow); }
  .field-clinic { top: 263px; }
  .field-clinic .field-line { left: 255px; background: var(--teal-light); }
  .field-signature { top: 325px; }
  .field-signature .field-line { left: 292px; background: var(--red); }

  .supplier {
    position: absolute; left: 176px; top: 409px; width: 510px; height: 41px;
    background: var(--dark); color: var(--white);
    display: flex; align-items: center; justify-content: center;
    font-size: 27px; font-weight: 500; letter-spacing: 0.3px;
  }
</style>
</head>
<body>

<section class="card card-front">
  <svg class="card-art" viewBox="0 0 700 410" preserveAspectRatio="none" aria-hidden="true">
    <defs>
      <linearGradient id="band-teal" x1="0" y1="0" x2="1" y2="0.3">
        <stop offset="0" stop-color="#17918a"/>
        <stop offset="1" stop-color="#6fb1ac"/>
      </linearGradient>
    </defs>
    <polygon fill="#262626" points="0,62 172,242 232,242 392,410 0,410"/>
    <polygon fill="#333333" points="0,96 156,258 216,258 352,410 0,410"/>
    <polygon fill="url(#band-teal)" points="0,0 62,0 232,188 232,242 172,242 0,62"/>
  </svg>

  <p class="ribbon ribbon-intro">The individual bearing this card&nbsp; has undergone weight loss surgery.</p>
  <p class="ribbon ribbon-restriction">This surgery restricts portion sizes to between&nbsp; half and one cup<br>of food at a time.</p>
  <p class="ribbon ribbon-request">Please give consideration to allowing smaller portions&nbsp; of your<br>regular meals to be ordered to reduce wastage and excess costs.</p>
  <p class="ribbon ribbon-example">Example: a half size portion priced at two thirds of usual cost.</p>

  <div class="clinic-name"><span class="clinic-dot"></span>Kestrel Clinic</div>
</section>

<section class="card card-back">
  <svg class="card-art" viewBox="0 0 700 410" preserveAspectRatio="none" aria-hidden="true">
    <polygon fill="#fdbf00" points="0,0 193,0 172,35 0,35"/>
    <polygon fill="#67aca7" points="193,0 250,0 229,35 172,35"/>
    <polygon fill="#d56060" points="250,0 330,0 308,35 229,35"/>
    <polygon fill="#333333" points="330,0 700,0 700,35 308,35"/>
  </svg>

  <div class="field field-name"><span class="field-label">Name:</span><span class="field-line"></span></div>
  <div class="field field-procedure"><span class="field-label">Procedure performed:</span><span class="field-line"></span></div>
  <div class="field field-date"><span class="field-label">Date of procedure (month/year):</span><span class="field-line"></span></div>
  <div class="field field-clinic"><span class="field-label">Treating Clinic Name:</span><span class="field-line"></span></div>
  <div class="field field-signature"><span class="field-label">Treating Clinic Signature:</span><span class="field-line"></span></div>

  <p class="supplier">bernardwhitlow.com.au</p>
</section>

</body>
</html>
```